Social Media Application Design - Android and IOS

I am ready to go live with new social media app however I am not comfortable with the current design. It is a not interactive or attractive enough. Please note the splash screen is a green, so preference would be to keep a green theme although I am more than happy to consider other colours that would improve the design.
The attachment has the app screens that need to be redesigned. They may not need massive changes , however keen to go live so looking for inspired designers to support with this project and many others that I have, including ongoing work on this app.
Target Market(s)
Millenials
Industry/Entity Type
Social
Colors
Designer to choose colors to be used in the design.
Requirements
Must have
- Please see attached document for screens that I would like redesigned. It needs to work with Android and IOS. I am looking for the design and not the functionality.
Nice to have
- Highly interactive design. Please see polling functionality of Loomrix.
Should not have
- should not be complicated - simplicity is the key

```html
<!DOCTYPE html>
<html lang="en">
<head>
<meta charset="utf-8">
<title>Question App Screens</title>
<link rel="stylesheet" href="https://fonts.googleapis.com/css2?family=Nunito+Sans:wght@400;600;700&display=swap">
<style>
:root{
  --green:#63cc5f;
  --green-deep:#3f9a2a;
  --page:#f3faf1;
  --panel:#f2f2f2;
  --card:#ffffff;
  --ink:#1d1d1d;
  --muted:#9b9b9b;
  --line:#e3e3e3;
  --radio-off:#d9d9d9;
  --alert:#f04a44;
}
*{box-sizing:border-box;margin:0;padding:0}
html,body{width:1200px;height:1200px;overflow:hidden}
body{background:var(--page);font-family:"Nunito Sans",sans-serif;color:var(--ink);position:relative}
.screen{position:absolute;width:372px;background:var(--panel);overflow:hidden}
.screen--post{left:178px;top:211px;height:778px}
.screen--filter{left:650px;top:211px;height:742px}
.abs{position:absolute}
.status{left:0;top:0;width:372px;height:22px;background:var(--card);font-size:12px;font-weight:600}
.status span{position:absolute;top:3px;line-height:16px}
.appbar{left:0;top:22px;width:372px;height:58px;background:var(--card)}
.appbar__title{position:absolute;left:0;right:0;top:18px;text-align:center;font-size:18px;font-weight:700;line-height:22px}
.appbar__back{position:absolute;left:22px;top:16px}
.card{position:absolute;left:16px;width:340px;background:var(--card);border-radius:6px;overflow:hidden}
.label{position:absolute;font-size:14px;font-weight:600;line-height:18px;white-space:nowrap}
.see-all{position:absolute;right:12px;font-size:14px;color:var(--muted);line-height:18px}
.chip{position:absolute;height:34px;width:104px;border-radius:17px;background:var(--green);color:#fff;font-size:14px;font-weight:600;line-height:34px;text-align:center}
.chip__remove{position:absolute;right:-4px;top:-6px;width:13px;height:13px;border-radius:50%;background:var(--alert);border:1.5px solid #fff}
.chip__remove::before,.chip__remove::after{content:"";position:absolute;left:2.5px;top:4.2px;width:5px;height:1.3px;background:#fff;transform:rotate(45deg)}
.chip__remove::after{transform:rotate(-45deg)}
.textarea{position:absolute;left:17px;top:43px;width:305px;height:101px;border:1px solid var(--line);border-radius:2px;padding:9px 10px;font-size:13px;color:#b5b5b5}
.segmented{position:absolute;left:19px;top:45px;width:298px;height:37px;border:1px solid var(--green);border-radius:19px;display:flex;overflow:hidden}
.segmented span{flex:0 0 auto;text-align:center;line-height:35px;font-size:14px;color:var(--muted)}
.segmented .is-active{background:var(--green);color:#fff;font-weight:600}
.upload{position:absolute;top:114px;width:130px;height:115px;border-radius:8px;background:#fff;box-shadow:0 1px 6px rgba(0,0,0,.08);display:flex;align-items:center;justify-content:center}
.upload__caption{position:absolute;top:249px;font-size:14px;color:var(--muted);width:150px;text-align:center}
.button{position:absolute;left:16px;width:340px;height:46px;border-radius:23px;background:var(--green);color:#fff;font-size:16px;line-height:46px;text-align:center;letter-spacing:.5px}
.radio{position:absolute;left:20px;width:22px;height:22px;border-radius:50%;background:var(--radio-off)}
.radio::after{content:"";position:absolute;left:5px;top:5px;width:12px;height:12px;border-radius:50%;background:#c4c4c4}
.radio.is-on{background:var(--green)}
.radio.is-on::after{background:var(--green-deep)}
.radio-label{position:absolute;left:61px;font-size:14px;font-weight:600;line-height:18px}
.slider__track{position:absolute;left:19px;top:19px;width:303px;height:5px;border-radius:3px;background:#e6e6e6}
.slider__fill{position:absolute;left:93px;top:18px;width:175px;height:7px;background:var(--green-deep)}
.slider__knob{position:absolute;top:11px;width:21px;height:21px;border-radius:50%;background:var(--green)}
.slider__knob::after{content:"";position:absolute;left:5px;top:5px;width:11px;height:11px;border-radius:50%;background:var(--green-deep)}
</style>
</head>
<body>

<section class="screen screen--post">
  <div class="abs status">
    <svg class="abs" style="left:6px;top:7px" width="17" height="9"><rect x="0" y="5" width="3" height="4" fill="#111"/><rect x="4" y="3.5" width="3" height="5.5" fill="#111"/><rect x="8" y="2" width="3" height="7" fill="#111"/><rect x="12" y="0" width="3" height="9" fill="#111"/></svg>
    <span style="left:26px">Nimbo</span>
    <svg class="abs" style="left:71px;top:6px" width="14" height="10"><path d="M1 3.5a9 9 0 0 1 12 0M3.3 5.8a5.5 5.5 0 0 1 7.4 0" stroke="#111" stroke-width="1.6" fill="none"/><circle cx="7" cy="8.4" r="1.4" fill="#111"/></svg>
    <span style="left:0;right:0;text-align:center">9:41 AM</span>
    <svg class="abs" style="left:295px;top:5px" width="7" height="11"><path d="M1 3l5 5-2.5 2V1L6 3 1 8" stroke="#111" stroke-width="1.2" fill="none"/></svg>
    <span style="left:306px">100%</span>
    <svg class="abs" style="left:341px;top:6px" width="26" height="11"><rect x=".5" y=".5" width="22" height="10" rx="2" stroke="#111" fill="none"/><rect x="2" y="2" width="19" height="7" rx="1" fill="#111"/><rect x="23.5" y="3.5" width="2" height="4" fill="#111"/></svg>
  </div>
  <header class="abs appbar">
    <svg class="appbar__back" width="14" height="26"><path d="M12 1L2 13l10 12" stroke="#333" stroke-width="1.6" fill="none"/></svg>
    <h1 class="appbar__title">Post a Questions</h1>
  </header>

  <div class="card" style="top:95px;height:111px">
    <p class="label" style="left:19px;top:21px">Your question is about</p>
    <a class="see-all" style="top:21px">see all</a>
    <span class="chip" style="left:19px;top:55px">Science</span>
    <span class="chip" style="left:139px;top:55px">Health</span>
    <span class="chip" style="left:258px;top:55px">Gadgets</span>
  </div>

  <div class="card" style="top:228px;height:163px">
    <p class="label" style="left:17px;top:11px">What is your Questions ?</p>
    <div class="textarea">Type text here....</div>
  </div>

  <div class="card" style="top:410px;height:283px">
    <p class="label" style="left:17px;top:11px">What are the options ?</p>
    <div class="segmented">
      <span class="is-active" style="width:104px">Images</span>
      <span style="width:94px;border-right:1px solid var(--green)">Text</span>
      <span style="width:98px">Audio</span>
    </div>
    <div class="upload" style="left:19px">
      <svg width="56" height="46"><path d="M4 12h12l5-8h14l5 8h12v30H4z" stroke="#d3d3d3" stroke-width="2.4" fill="none" stroke-linejoin="round"/><circle cx="28" cy="26" r="10" stroke="#d3d3d3" stroke-width="2.4" fill="none"/></svg>
    </div>
    <div class="upload" style="left:183px">
      <svg width="56" height="46"><path d="M4 12h12l5-8h14l5 8h12v30H4z" stroke="#d3d3d3" stroke-width="2.4" fill="none" stroke-linejoin="round"/><circle cx="28" cy="26" r="10" stroke="#d3d3d3" stroke-width="2.4" fill="none"/></svg>
    </div>
    <p class="upload__caption" style="left:20px">Upload Option 1</p>
    <p class="upload__caption" style="left:168px">Upload Option 2</p>
  </div>

  <div class="button" style="top:713px">POST</div>
</section>

<section class="screen screen--filter">
  <div class="abs status">
    <svg class="abs" style="left:6px;top:7px" width="17" height="9"><rect x="0" y="5" width="3" height="4" fill="#111"/><rect x="4" y="3.5" width="3" height="5.5" fill="#111"/><rect x="8" y="2" width="3" height="7" fill="#111"/><rect x="12" y="0" width="3" height="9" fill="#111"/></svg>
    <span style="left:26px">Nimbo</span>
    <svg class="abs" style="left:71px;top:6px" width="14" height="10"><path d="M1 3.5a9 9 0 0 1 12 0M3.3 5.8a5.5 5.5 0 0 1 7.4 0" stroke="#111" stroke-width="1.6" fill="none"/><circle cx="7" cy="8.4" r="1.4" fill="#111"/></svg>
    <span style="left:0;right:0;text-align:center">9:41 AM</span>
    <svg class="abs" style="left:295px;top:5px" width="7" height="11"><path d="M1 3l5 5-2.5 2V1L6 3 1 8" stroke="#111" stroke-width="1.2" fill="none"/></svg>
    <span style="left:306px">100%</span>
    <svg class="abs" style="left:341px;top:6px" width="26" height="11"><rect x=".5" y=".5" width="22" height="10" rx="2" stroke="#111" fill="none"/><rect x="2" y="2" width="19" height="7" rx="1" fill="#111"/><rect x="23.5" y="3.5" width="2" height="4" fill="#111"/></svg>
  </div>
  <header class="abs appbar" style="height:57px">
    <svg class="appbar__back" width="14" height="26"><path d="M12 1L2 13l10 12" stroke="#333" stroke-width="1.6" fill="none"/></svg>
    <h1 class="appbar__title">QZLY</h1>
  </header>

  <div class="card" style="top:88px;height:111px;overflow:visible">
    <p class="label" style="left:19px;top:21px">Your question is about</p>
    <a class="see-all" style="top:21px">see all</a>
    <span class="chip" style="left:19px;top:55px">Science<i class="chip__remove"></i></span>
    <span class="chip" style="left:139px;top:55px">Health<i class="chip__remove"></i></span>
    <div style="position:absolute;left:258px;top:55px;width:82px;height:34px;overflow:hidden;border-radius:17px 0 0 17px">
      <span class="chip" style="left:0;top:0">Gadgets</span>
    </div>
  </div>

  <div class="card" style="top:217px;height:120px">
    <p class="label" style="left:17px;top:11px">Questions</p>
    <i class="radio is-on" style="top:43px"></i><p class="radio-label" style="top:45px">My Questions</p>
    <i class="radio" style="top:78px"></i><p class="radio-label" style="top:80px">All Questions</p>
  </div>

  <div class="card" style="top:355px;height:111px">
    <p class="label" style="left:17px;top:11px">Location (Limit Search To)</p>
    <div style="position:absolute;left:0;top:36px;width:340px;height:40px">
      <div class="slider__track"></div>
      <div class="slider__fill"></div>
      <i class="slider__knob" style="left:102px"></i>
      <i class="slider__knob" style="left:277px"></i>
    </div>
    <p class="label" style="left:17px;top:74px">5km</p>
    <p class="label" style="right:18px;top:74px">65km</p>
  </div>

  <div class="card" style="top:484px;height:157px">
    <p class="label" style="left:17px;top:11px">Sort By</p>
    <i class="radio is-on" style="top:43px"></i><p class="radio-label" style="top:45px">Newest</p>
    <i class="radio" style="top:78px"></i><p class="radio-label" style="top:80px">Popular</p>
    <i class="radio" style="top:113px"></i><p class="radio-label" style="top:115px">Trending</p>
  </div>

  <div class="button" style="top:661px;height:45px;line-height:45px">APPLY</div>
</section>

</body>
</html>
```